Label for packages of Pure Raw Natural Honeycomb

This is a label that will be used to sell pure raw honeycomb on the internet and in farm gate sales
Label must contain my Logo (which is attached)
my website www.meadowglintfarm.ca
the weight 300 gr and the words Pure Raw Honeycomb
label design should fit onto a sticker 3" by 2" oval but If the size appears to small to get all that info on I am willing to look at a different size or shape

Target Market(s)

internet and in person farm gate customers

Industry/Entity Type

Agriculture

Font styles to use
Other font styles liked:
• the font should compliment my logo font

Colors
ffc214

Requirements
Must have
• Label must contain my Logo (attached) my website www.meadowglintfarm.ca
• the weight 300 gr and the words Pure Raw Honeycomb would like something in black and gold with a bit of an Elegant vintage feel
Nice to have
• vintage feel
• If the size appears to small to get all that info on I am willing to look at a different size or shape
Should not have
• no cartoons

```html
<!DOCTYPE html>
<html lang="en">
<head>
<meta charset="utf-8">
<title>Meadowglint Farm – Pure Raw Honeycomb Label</title>
<link rel="stylesheet" href="https://fonts.googleapis.com/css2?family=Cinzel:wght@400&family=Lobster&display=block">
<style>
  :root {
    --gold: #ffc214;
    --label-dark: #2a2a2a;
    --label-dark-edge: #1c1c1c;
    --paper: #ffffff;
  }
  html, body {
    margin: 0;
    padding: 0;
    width: 1200px;
    height: 1200px;
    overflow: hidden;
    background: var(--paper);
  }
  .label {
    display: block;
    width: 1200px;
    height: 1200px;
  }
  .label__rim { fill: var(--gold); }
  .label__title {
    font-family: "Lobster", cursive;
    font-size: 70px;
    fill: var(--gold);
  }
  .brand__mark {
    fill: none;
    stroke: var(--gold);
    stroke-width: 7;
  }
  .brand__name {
    font-family: "Lobster", cursive;
    font-size: 82px;
    fill: var(--gold);
  }
  .label__weight,
  .label__website {
    font-family: "Cinzel", serif;
    fill: var(--gold);
  }
  .label__weight { font-size: 26px; letter-spacing: 2px; }
  .label__website { font-size: 24px; letter-spacing: 1px; }
</style>
</head>
<body>
<svg class="label" viewBox="0 0 1200 1200" xmlns="http://www.w3.org/2000/svg">
  <defs>
    <radialGradient id="label-face" cx="50%" cy="45%" r="60%">
      <stop offset="0%" stop-color="#2a2a2a"/>
      <stop offset="100%" stop-color="#1c1c1c"/>
    </radialGradient>
    <path id="title-arc" d="M 262 420 Q 600 230 948 420"/>
  </defs>

  <ellipse class="label__rim" cx="600" cy="600" rx="582" ry="366"/>
  <ellipse class="label__face" cx="600" cy="600" rx="560" ry="344" fill="url(#label-face)"
           role="img" aria-label="Dark charcoal field with a faint honeycomb texture and a gold wavy ornamental border"/>

  <text class="label__title">
    <textPath href="#title-arc" startOffset="50%" text-anchor="middle">Pure Raw Honeycomb</textPath>
  </text>

  <g class="brand">
    <circle class="brand__mark" cx="600" cy="545" r="80"/>
    <text class="brand__name" x="600" y="735" text-anchor="middle">Meadowglint Farm</text>
  </g>

  <text class="label__weight" x="600" y="842" text-anchor="middle">300 G</text>
  <text class="label__website" x="600" y="900" text-anchor="middle">WWW.MEADOWGLINTFARM.CA</text>
</svg>
</body>
</html>
```